ALL TEXT Social Media Graphics

We are looking for a series of social media graphics for Instagram (new size: 4:5 (1080 x 1350 pixels) ratio that are ALL TEXT. We want the following quotes below on each graphic; one quote per graphic. AND, In very small letters at the bottom of each graphic, add @PaulaWrenLive
The look and feel of these graphics should be complimentary to the color palette attached below; but keep them simple. But the design is up to you; at the end of this document, I provided various samples of all text graphics that I like as examples.
The Quotes are in the attached WORD document
women trying to lose weight

```html
<!DOCTYPE html>
<html lang="en">
<head>
<meta charset="utf-8">
<title>Sunlit Body Reset – Text Graphics</title>
<link rel="stylesheet" href="https://fonts.googleapis.com/css2?family=Oswald:wght@300;400;600&family=Italiana&family=Open+Sans:wght@400&display=swap">
<style>
  :root {
    --backdrop: #fbbde0;
    --card: #ffffff;
    --pink-soft: #f48fb6;
    --pink: #f0619a;
    --berry: #b0155a;
    --ink: #111111;
  }
  html, body {
    margin: 0;
    padding: 0;
    width: 1200px;
    height: 753px;
    overflow: hidden;
    background: var(--backdrop);
  }
  .board { display: block; width: 1200px; height: 753px; }
  .card { fill: var(--card); }
  .headline { font-family: "Oswald", "Arial Narrow", sans-serif; font-weight: 600; }
  .callout { font-family: "Oswald", "Arial Narrow", sans-serif; font-weight: 300; fill: var(--berry); }
  .callout .keyword { font-weight: 600; }
  .tagline { font-family: "Italiana", "Times New Roman", serif; fill: var(--ink); }
  .handle { font-family: "Open Sans", Arial, sans-serif; fill: var(--ink); }
  .centered { text-anchor: middle; }
  .soft { fill: var(--pink-soft); }
  .pink { fill: var(--pink); }
  .berry { fill: var(--berry); }
</style>
</head>
<body>
<svg class="board" viewBox="0 0 2150 1350" xmlns="http://www.w3.org/2000/svg" role="img" aria-label="Five text graphics promoting the Sunlit Body Reset">
  <!-- Feature card -->
  <rect class="card" x="45" y="53" width="995" height="1245"/>
  <g class="feature">
    <text class="headline pink" x="125" y="222" font-size="125" textLength="820" lengthAdjust="spacingAndGlyphs">YOU CAN ABSOLUTELY</text>
    <text class="headline pink" x="148" y="432" font-size="270" textLength="797" lengthAdjust="spacingAndGlyphs">BE DOWN</text>
    <text class="headline berry" x="138" y="572" font-size="165" textLength="820" lengthAdjust="spacingAndGlyphs">20–30 POUNDS</text>
    <text class="headline pink" x="135" y="688" font-size="130" textLength="827" lengthAdjust="spacingAndGlyphs">BY END OF SUMMER</text>
    <text class="tagline" x="287" y="795" font-size="72" textLength="513" lengthAdjust="spacingAndGlyphs">ALL IT TAKES IS</text>
    <text class="tagline berry" x="275" y="870" font-size="72" textLength="537" lengthAdjust="spacingAndGlyphs">THE RIGHT PLAN</text>
    <text class="tagline" x="175" y="943" font-size="72" textLength="740" lengthAdjust="spacingAndGlyphs">AND YOU’VE FOUND IT.</text>
    <text class="callout centered" x="542" y="1055" font-size="84">Comment <tspan class="keyword">GLOW</tspan> for the Sunlit</text>
    <text class="callout centered" x="542" y="1125" font-size="84">Body Reset!</text>
    <text class="handle" x="115" y="1226" font-size="42">@PaulaWrenLive</text>
  </g>

  <!-- Card: system that works -->
  <rect class="card" x="1091" y="53" width="483" height="603"/>
  <g>
    <text class="headline soft" x="1125" y="150" font-size="80" textLength="413" lengthAdjust="spacingAndGlyphs">YOU DON’T NEED</text>
    <text class="headline pink" x="1125" y="225" font-size="90" textLength="420" lengthAdjust="spacingAndGlyphs">ANOTHER DIET</text>
    <text class="headline pink" x="1122" y="270" font-size="52" textLength="421" lengthAdjust="spacingAndGlyphs">YOU NEED A SYSTEM THAT</text>
    <text class="headline berry" x="1140" y="403" font-size="167" textLength="392" lengthAdjust="spacingAndGlyphs">WORKS</text>
    <text class="tagline" x="1148" y="447" font-size="36" textLength="369" lengthAdjust="spacingAndGlyphs">DROP <tspan class="pink">30 POUNDS</tspan> WITH</text>
    <text class="tagline centered" x="1332" y="483" font-size="36">THE SUNLIT BODY</text>
    <text class="tagline centered" x="1332" y="518" font-size="36">RESET.</text>
    <text class="callout" x="1130" y="573" font-size="42" textLength="405" lengthAdjust="spacingAndGlyphs">Comment <tspan class="keyword">SUMMER</tspan> to start now.</text>
    <text class="handle" x="1125" y="622" font-size="20">@PaulaWrenLive</text>
  </g>

  <!-- Card: tiny waist -->
  <rect class="card" x="1622" y="53" width="483" height="603"/>
  <g>
    <text class="headline soft" x="1660" y="170" font-size="83" textLength="410" lengthAdjust="spacingAndGlyphs">IF YOUR GOAL IS</text>
    <text class="headline berry" x="1662" y="250" font-size="97" textLength="406" lengthAdjust="spacingAndGlyphs">A TINY WAIST</text>
    <text class="headline pink" x="1662" y="345" font-size="111" textLength="410" lengthAdjust="spacingAndGlyphs">FLAT BELLY</text>
    <text class="headline berry" x="1660" y="397" font-size="62" textLength="408" lengthAdjust="spacingAndGlyphs"><tspan class="soft">AND</tspan> 30 POUNDS DOWN</text>
    <text class="tagline" x="1678" y="467" font-size="50" textLength="372" lengthAdjust="spacingAndGlyphs">THIS IS <tspan class="pink">THE PLAN</tspan></text>
    <text class="callout centered" x="1863" y="532" font-size="42">Comment <tspan class="keyword">SUMMER</tspan> to join</text>
    <text class="callout centered" x="1863" y="567" font-size="42">the Sunlit Body Reset!</text>
    <text class="handle" x="1657" y="622" font-size="20">@PaulaWrenLive</text>
  </g>

  <!-- Card: summer ain't over -->
  <rect class="card" x="1091" y="694" width="483" height="603"/>
  <g>
    <text class="headline berry" x="1128" y="800" font-size="90" textLength="405" lengthAdjust="spacingAndGlyphs">THIS SUMMER</text>
    <text class="headline berry" x="1130" y="890" font-size="108" textLength="403" lengthAdjust="spacingAndGlyphs">AIN’T OVER</text>
    <text class="headline pink" x="1128" y="940" font-size="58" textLength="407" lengthAdjust="spacingAndGlyphs">AND NEITHER ARE YOUR</text>
    <text class="headline pink" x="1128" y="1020" font-size="100" textLength="410" lengthAdjust="spacingAndGlyphs">BODY GOALS</text>
    <text class="tagline" x="1148" y="1073" font-size="36" textLength="369" lengthAdjust="spacingAndGlyphs">DROP <tspan class="pink">30 POUNDS</tspan> WITH</text>
    <text class="tagline centered" x="1332" y="1109" font-size="36">THE SUNLIT BODY</text>
    <text class="tagline centered" x="1332" y="1144" font-size="36">RESET.</text>
    <text class="callout centered" x="1332" y="1195" font-size="42">Comment <tspan class="keyword">GLOW</tspan> to get</text>
    <text class="callout centered" x="1332" y="1228" font-size="42">the plan</text>
    <text class="handle" x="1125" y="1263" font-size="20">@PaulaWrenLive</text>
  </g>

  <!-- Card: still time -->
  <rect class="card" x="1622" y="694" width="483" height="603"/>
  <g>
    <text class="headline pink" x="1652" y="800" font-size="70" textLength="423" lengthAdjust="spacingAndGlyphs">THERE’S STILL TIME</text>
    <text class="headline soft" x="1652" y="880" font-size="100" textLength="423" lengthAdjust="spacingAndGlyphs">TO DROP THE</text>
    <text class="headline berry" x="1655" y="973" font-size="111" textLength="422" lengthAdjust="spacingAndGlyphs">30 POUNDS</text>
    <text class="headline pink" x="1652" y="1025" font-size="56" textLength="423" lengthAdjust="spacingAndGlyphs">AND SLAY THIS SUMMER</text>
    <text class="tagline centered" x="1863" y="1080" font-size="36">THE <tspan class="pink">SUNLIT BODY</tspan></text>
    <text class="tagline centered" x="1863" y="1116" font-size="36"><tspan class="pink">RESET</tspan> HAS THE</text>
    <text class="tagline centered" x="1863" y="1151" font-size="36">BLUEPRINT.</text>
    <text class="callout centered" x="1863" y="1207" font-size="42">Comment <tspan class="keyword">GLOW</tspan>!</text>
    <text class="handle" x="1657" y="1263" font-size="20">@PaulaWrenLive</text>
  </g>
</svg>
</body>
</html>
```